Book cover for LM

Design cover for a book of gratitude and inspiration.
Book trim size will be 6.5 x 6.5 inches, or 8 x 8 inches, hardcover, 96 pages
Title: Lantern Meadows
Subtitle: A Book of Gratitude and Inspiration
Author: Gus Halverd

```html
<!DOCTYPE html>
<html lang="en">
<head>
<meta charset="UTF-8">
<title>Lantern Meadows — Book Cover</title>
<link href="https://fonts.googleapis.com/css2?family=Kaushan+Script&family=Montserrat:wght@500;600;700&display=swap" rel="stylesheet">
<style>
  :root {
    --sky-top: #d9502a;
    --sky-mid: #ea6a2a;
    --glow-core: #ffe58a;
    --glow-warm: #f6a13a;
    --dusk: #1a1512;
    --night: #050404;
    --title-white: #ffffff;
    --title-shadow: #f7941d;
    --ink-dark: #1d1410;
    --author-orange: #f7941d;
    --subtitle-white: #ffffff;
  }
  * { margin: 0; padding: 0; box-sizing: border-box; }
  html, body {
    width: 1200px;
    height: 1200px;
    overflow: hidden;
    background: var(--night);
  }
  .cover {
    position: relative;
    width: 1200px;
    height: 1200px;
    overflow: hidden;
  }
  .cover-photo {
    position: absolute;
    inset: 0;
    background:
      radial-gradient(ellipse 300px 260px at 600px 610px, var(--glow-core) 0%, rgba(246,161,58,0.85) 35%, rgba(234,106,42,0) 100%),
      linear-gradient(to bottom, var(--sky-top) 0%, var(--sky-mid) 45%, #b4532a 62%, var(--dusk) 78%, var(--night) 100%);
  }
  .title-kicker {
    position: absolute;
    z-index: 2;
    left: 590px;
    top: 146px;
    font-family: "Montserrat", sans-serif;
    font-weight: 600;
    font-size: 62px;
    letter-spacing: 1px;
    color: var(--ink-dark);
    line-height: 1;
  }
  .title-main {
    position: absolute;
    z-index: 1;
    left: 0;
    width: 1200px;
    top: 188px;
    text-align: center;
    font-family: "Kaushan Script", cursive;
    font-size: 240px;
    font-weight: 400;
    line-height: 1.2;
    color: var(--title-white);
    text-shadow: 10px 10px 0 var(--title-shadow);
  }
  .subtitle {
    position: absolute;
    left: 0;
    width: 1200px;
    top: 1010px;
    text-align: center;
    font-family: "Montserrat", sans-serif;
    font-weight: 500;
    font-size: 36px;
    color: var(--subtitle-white);
    line-height: 1;
  }
  .author {
    position: absolute;
    left: 0;
    width: 1200px;
    top: 1078px;
    text-align: center;
    font-family: "Montserrat", sans-serif;
    font-weight: 700;
    font-size: 66px;
    color: var(--author-orange);
    line-height: 1;
  }
</style>
</head>
<body>
  <main class="cover">
    <div class="cover-photo" role="img" aria-label="Photograph of a single wildflower with green petals perched on a dark rock, backlit by a glowing orange sunset sky"></div>
    <div class="title-kicker">LANTERN</div>
    <h1 class="title-main">Meadows</h1>
    <p class="subtitle">A BOOK OF GRATITUDE AND INSPIRATION</p>
    <p class="author">GUS HALVERD</p>
  </main>
</body>
</html>
```